I have a PHP web application to manage IT support calls and require a front-end design and user logon screen.

I have attached the current design which needs improving.

I have 2 current designs. The 2nd design is one I have been working on but requires a "professional touch". I also require the tables designed with dummy data from the 1st design.

I have attached my company logo in AI format which I would like incorporated into the design. There should also be a placeholder to supply the users company name upon login.

The screenshots I have attached should explain what I am looking for.

The Home Page should include charts which show statistical information such as:
Number of support tickets logged per month. Bar Chart etc.
Number of currently open support tickets.
Number of Quote Requests awaiting a response.
Number of Files and file repository.
Number of Reports.
Number of Customers.

For the Jobs and Customers pages the table fields should be designed as per the attached screenshots but a better looking tables. The table options such as uploading a file and adding a customer - these options can be changed and displayed differently.

Quotes page should display quotes returned and a "request a quote form".

Files page should have a good structure for browsing through an archive of files.

Profile page should have the option to include a profile picture.

An additional side page should be created for a web based calendar (these calendar entries will be updated by code).

The navbar should also include an alerts section.
The current attached design I have is based on bootstraps navbar.

Inspiration: http://plenvaro.com/freebie/free-admin-templates-for-backend-panels/

Hopefully this above link will show you some navigation style designs that I am looking for.

Please note, I will be doing the PHP coding myself and it is just the page designs I require in either HTML and or PHP format. I also require the CSS files for this project.
I need the code in a format where I can add and remove items in the menu from the code and not PSD/image based format.

If you think this project requires a higher budget let me know what you would expect and I will increase it!

Any questions, please let me know.
Dummy data can be shown for design purposes.

I have provided you a dummy login to our current system to show you the system:
https://reef.vomilbrixtonsolutions.co.uk/
username: dan.hollow@vomilbrixtonsolutions.co.uk
password:K#72zqTm

```html
<!DOCTYPE html>
<html lang="en">
<head>
<meta charset="utf-8">
<title>Reef – Call out and support tracker</title>
<link rel="stylesheet" href="https://fonts.googleapis.com/css2?family=Roboto:wght@300;400;500;700&display=swap">
<style>
:root{
  --navy:#2b2f3d;
  --sidebar:#2d303c;
  --sidebar-line:#3a3e4b;
  --active:#3b8fe3;
  --canvas:#eceef1;
  --panel:#ffffff;
  --border:#d9dce1;
  --text:#333743;
  --muted:#8a8f9a;
  --red:#e84545;
  --green:#3bb54a;
  --blue:#3b8fe3;
  --pink:#f38a88;
  --table-head:#d4d6da;
  --row-alt:#f0f1f3;
}
*{box-sizing:border-box;margin:0;padding:0}
html,body{width:774px;height:1200px;overflow:hidden}
body{font-family:"Roboto",Arial,sans-serif;color:var(--text);background:var(--canvas);position:relative;font-size:8px}

.topbar{position:absolute;left:0;top:0;width:774px;height:58px;background:#fff;border-bottom:1px solid var(--border);display:flex;align-items:center}
.brand{width:168px;height:58px;display:flex;align-items:center;gap:7px;padding-left:14px}
.brand-mark{width:16px;height:16px;border-radius:50%;background:var(--active)}
.brand-name{font-size:15px;font-weight:400;color:var(--navy)}
.app-title{font-size:13px;font-weight:500;color:var(--navy)}
.app-title span{font-weight:300;font-size:9px;color:var(--muted);margin-left:4px}
.user{margin-left:auto;display:flex;align-items:center;gap:6px;font-size:9px;padding-right:18px}
.user-avatar{width:24px;height:24px;border-radius:50%;background:linear-gradient(#8a7a70,#4a403b)}
.user .caret{color:var(--muted);margin-right:22px}

.sidebar{position:absolute;left:0;top:58px;width:74px;height:1090px;background:var(--sidebar)}
.nav a{display:flex;align-items:center;gap:6px;height:24px;padding-left:8px;color:#d3d6dc;text-decoration:none;font-size:8px;border-bottom:1px solid var(--sidebar-line)}
.nav a.active{background:var(--active);color:#fff}
.nav svg{width:9px;height:9px;fill:currentColor}

.panel{position:absolute;background:var(--panel);border:1px solid var(--border)}
.panel-head{height:24px;background:var(--navy);color:#fff;font-size:9px;font-weight:500;display:flex;align-items:center;padding-left:8px}

.tickets{left:85px;top:85px;width:360px;height:212px}
.linechart{left:464px;top:85px;width:292px;height:212px}
.chart{display:block;margin:8px 8px 0}
.axis{font-size:7px;fill:var(--muted)}

.open{left:85px;top:317px;width:360px;height:194px}
.ticket{display:flex;gap:8px;padding:10px 10px 0}
.ticket-thumb{width:34px;height:30px;background:linear-gradient(90deg,#6aa84f,#c9a44a,#7c5fa8)}
.ticket p{font-size:8px;color:var(--text);line-height:1.3}
.ticket time{font-size:6.5px;color:var(--muted)}

.reports{left:464px;top:317px;width:292px;height:194px}
.gauges{display:flex;justify-content:space-around;padding-top:22px}
.gauge{text-align:center}
.gauge svg{display:block;margin:0 auto 10px}
.gauge text{font-size:11px}
.btn{display:inline-block;padding:5px 10px;color:#fff;font-size:7px;border-radius:2px}
.btn-red{background:var(--red)}.btn-green{background:var(--green)}.btn-blue{background:var(--blue)}

.files{left:85px;top:560px;width:671px;height:317px}
.files table{width:615px;margin:20px auto 0;border-collapse:collapse;font-size:7px}
.files th{background:var(--table-head);height:20px;font-weight:400}
.files td{height:25px;text-align:center;border-bottom:1px solid #fff}
.files tbody tr:nth-child(odd){background:var(--row-alt)}
.files tbody tr:nth-child(even){background:#fafafa}
.icons{display:inline-flex;gap:3px}
.icons i{width:9px;height:8px;background:#fff;border:1px solid #bbb;display:inline-block}
.file-actions{position:absolute;right:28px;bottom:22px;display:flex;gap:16px}
.file-actions .btn{padding:7px 16px}

.quotes{left:85px;top:910px;width:515px;height:206px}
.quote{display:flex;align-items:center;gap:6px;padding:0 8px;height:24px;border-bottom:1px solid #eee;font-size:6.5px;color:var(--muted)}
.quote i{width:9px;height:9px;display:inline-block;flex:none}
.quote p{flex:1}
.quote .btn{padding:3px 5px;font-size:6px}

.customers{left:614px;top:910px;width:142px;height:206px}
.customer{display:flex;align-items:center;gap:8px;padding:10px 10px 0 18px}
.customer-avatar{width:26px;height:26px;border-radius:50%;background:linear-gradient(#c7b2a4,#7b6a62)}
.customer b{display:block;font-size:8px;font-weight:500}
.customer small{font-size:6.5px;color:var(--green)}
.view-all{position:absolute;right:10px;bottom:10px;font-size:7.5px;color:var(--blue)}

.footer{position:absolute;left:0;top:1148px;width:774px;height:52px;background:var(--navy);color:#cfd2d8;font-size:7px;display:flex;align-items:center;justify-content:center}
.footer span{position:absolute;right:12px}
</style>
</head>
<body>

<header class="topbar">
  <div class="brand"><span class="brand-mark"></span><span class="brand-name">Brixton</span></div>
  <div class="app-title">Reef <span>| Call out and support tracker</span></div>
  <div class="user">
    <div class="user-avatar" role="img" aria-label="User profile photo"></div>
    <span>Martin Delacroix</span><span class="caret">▾</span><span>Help</span>
  </div>
</header>

<aside class="sidebar">
  <nav class="nav">
    <a class="active" href="#"><svg viewBox="0 0 10 10"><path d="M5 1 1 5h1.5v4h2V6.5h1V9h2V5H9z"/></svg>Home</a>
    <a href="#"><svg viewBox="0 0 10 10"><rect x="1" y="3" width="8" height="6"/><rect x="3.5" y="1" width="3" height="2"/></svg>Jobs</a>
    <a href="#"><svg viewBox="0 0 10 10"><circle cx="5" cy="3" r="2"/><path d="M1 9c0-3 8-3 8 0z"/></svg>Customers</a>
    <a href="#"><svg viewBox="0 0 10 10"><rect x="1" y="1" width="8" height="8"/></svg>Inventory</a>
    <a href="#"><svg viewBox="0 0 10 10"><rect x="1" y="5" width="2" height="4"/><rect x="4" y="2" width="2" height="7"/><rect x="7" y="4" width="2" height="5"/></svg>Reports</a>
    <a href="#"><svg viewBox="0 0 10 10"><path d="M1 2h3l1 1h4v6H1z"/></svg>Files</a>
  </nav>
</aside>

<section class="panel tickets">
  <div class="panel-head">Support Tickets Logged per Month</div>
  <svg class="chart" width="342" height="172" viewBox="0 0 342 172">
    <g class="axis"><text x="0" y="20">500</text><text x="0" y="50">400</text><text x="0" y="80">300</text><text x="0" y="110">200</text><text x="0" y="140">100</text></g>
    <g stroke="#e4e6ea"><line x1="20" y1="17" x2="340" y2="17"/><line x1="20" y1="47" x2="340" y2="47"/><line x1="20" y1="77" x2="340" y2="77"/><line x1="20" y1="107" x2="340" y2="107"/><line x1="20" y1="137" x2="340" y2="137"/></g>
    <path d="M22 137 L22 80 L70 55 L110 30 L150 85 L190 65 L230 40 L270 75 L310 95 L338 60 L338 137 Z" fill="var(--pink)"/>
    <g class="axis"><text x="18" y="156">JAN</text><text x="80" y="156">MAR</text><text x="145" y="156">MAY</text><text x="208" y="156">JUL</text><text x="268" y="156">SEP</text><text x="322" y="156">NOV</text></g>
  </svg>
</section>

<section class="panel linechart">
  <div class="panel-head">Bar Chart</div>
  <svg class="chart" width="276" height="172" viewBox="0 0 276 172">
    <g stroke="#e4e6ea"><line x1="0" y1="17" x2="276" y2="17"/><line x1="0" y1="47" x2="276" y2="47"/><line x1="0" y1="77" x2="276" y2="77"/><line x1="0" y1="107" x2="276" y2="107"/><line x1="0" y1="137" x2="276" y2="137"/></g>
    <polyline fill="none" stroke="#9bd49d" stroke-width="1.5" points="8,40 45,100 85,70 125,120 165,30 205,95 245,50 270,80"/>
    <polyline fill="none" stroke="#f29a9a" stroke-width="1.5" points="8,110 45,60 85,115 125,55 165,100 205,45 245,120 270,65"/>
    <g fill="var(--green)"><circle cx="8" cy="40" r="3"/><circle cx="45" cy="100" r="3"/><circle cx="85" cy="70" r="3"/><circle cx="125" cy="120" r="3"/><circle cx="165" cy="30" r="3"/><circle cx="205" cy="95" r="3"/><circle cx="245" cy="50" r="3"/><circle cx="270" cy="80" r="3"/></g>
    <g fill="var(--red)"><circle cx="8" cy="110" r="3"/><circle cx="45" cy="60" r="3"/><circle cx="85" cy="115" r="3"/><circle cx="125" cy="55" r="3"/><circle cx="165" cy="100" r="3"/><circle cx="205" cy="45" r="3"/><circle cx="245" cy="120" r="3"/><circle cx="270" cy="65" r="3"/></g>
    <g class="axis"><text x="2" y="156">JAN</text><text x="58" y="156">MAR</text><text x="118" y="156">MAY</text><text x="176" y="156">JUL</text><text x="226" y="156">SEP</text><text x="256" y="156">NOV</text></g>
  </svg>
</section>

<section class="panel open">
  <div class="panel-head">Currently Open Support Tickets</div>
  <div class="ticket"><div class="ticket-thumb" role="img" aria-label="Ticket attachment thumbnail"></div><div><p>Lorem ipsum dolor sit ullamco et</p><time>May 16,2014</time></div></div>
  <div class="ticket"><div class="ticket-thumb" role="img" aria-label="Ticket attachment thumbnail"></div><div><p>Ut wisi enim ad minim veniam, quis nostrud exerci</p><time>May 16,2014</time></div></div>
  <div class="ticket"><div class="ticket-thumb" role="img" aria-label="Ticket attachment thumbnail"></div><div><p>Claritas est etiam processus dynamicus, qui</p><time>May 16,2014</time></div></div>
</section>

<section class="panel reports">
  <div class="panel-head">Reports</div>
  <div class="gauges">
    <div class="gauge">
      <svg width="56" height="56" viewBox="0 0 56 56"><circle cx="28" cy="28" r="24" fill="none" stroke="var(--red)" stroke-width="2"/><text x="28" y="32" text-anchor="middle" fill="var(--red)">76%</text></svg>
      <span class="btn btn-red">Transactions</span>
    </div>
    <div class="gauge">
      <svg width="56" height="56" viewBox="0 0 56 56"><circle cx="28" cy="28" r="24" fill="none" stroke="var(--green)" stroke-width="2"/><text x="28" y="32" text-anchor="middle" fill="var(--green)">88%</text></svg>
      <span class="btn btn-green">View Visits</span>
    </div>
    <div class="gauge">
      <svg width="56" height="56" viewBox="0 0 56 56"><circle cx="28" cy="28" r="24" fill="none" stroke="var(--blue)" stroke-width="2"/><text x="28" y="32" text-anchor="middle" fill="var(--blue)">65%</text></svg>
      <span class="btn btn-blue">Session</span>
    </div>
  </div>
</section>

<section class="panel files">
  <div class="panel-head">Files and File Repository</div>
  <table>
    <thead><tr><th>File</th><th>Label 1</th><th>Label 2</th><th>Label 3</th><th>Label 4</th><th>Label 5</th><th>Actions</th></tr></thead>
    <tbody>
      <tr><td>File 1</td><td>Data</td><td>Data</td><td>Data</td><td>Data</td><td>Data</td><td><span class="icons"><i></i><i></i></span></td></tr>
      <tr><td>File 2</td><td>Data</td><td>Data</td><td>Data</td><td>Data</td><td>Data</td><td><span class="icons"><i></i><i></i></span></td></tr>
      <tr><td>File 3</td><td>Data</td><td>Data</td><td>Data</td><td>Data</td><td>Data</td><td><span class="icons"><i></i><i></i></span></td></tr>
      <tr><td>File 4</td><td>Data</td><td>Data</td><td>Data</td><td>Data</td><td>Data</td><td><span class="icons"><i></i><i></i></span></td></tr>
      <tr><td>File 5</td><td>Data</td><td>Data</td><td>Data</td><td>Data</td><td>Data</td><td><span class="icons"><i></i><i></i></span></td></tr>
    </tbody>
  </table>
  <div class="file-actions"><span class="btn btn-red">Delete</span><span class="btn btn-blue">Build</span><span class="btn btn-green">Create</span></div>
</section>

<section class="panel quotes">
  <div class="panel-head">Quote Requests Awaiting a Response</div>
  <div class="quote"><i style="background:var(--green)"></i><p>Lorem ipsum dolor sit amet, consectetuer adipiscing elit, sed diam nonummy nibh</p><span class="btn btn-red">Add quote</span></div>
  <div class="quote"><i style="background:var(--red)"></i><p>Ut wisi enim ad minim veniam, quis nostrud exerci tation ullamcorper suscipit lobortis</p><span class="btn btn-red">Add quote</span></div>
  <div class="quote"><i style="background:var(--blue)"></i><p>Duis autem vel eum iriure dolor in hendrerit in vulputate velit esse molestie</p><span class="btn btn-red">Add quote</span></div>
  <div class="quote"><i style="background:#f1b83a"></i><p>Nam liber tempor cum soluta nobis eleifend option congue nihil imperdiet doming</p><span class="btn btn-red">Add quote</span></div>
  <div class="quote"><i style="background:var(--green)"></i><p>Typi non habent claritatem insitam, est usus legentis in iis qui facit</p><span class="btn btn-red">Add quote</span></div>
</section>

<section class="panel customers">
  <div class="panel-head">Customers</div>
  <div class="customer"><div class="customer-avatar" role="img" aria-label="Customer profile photo"></div><div><b>Owen Harlow</b><small>● online</small></div></div>
  <div class="customer"><div class="customer-avatar" role="img" aria-label="Customer profile photo"></div><div><b>Nina Calder</b><small>● online</small></div></div>
  <div class="customer"><div class="customer-avatar" role="img" aria-label="Customer profile photo"></div><div><b>Paul Ferris</b><small>● online</small></div></div>
  <a class="view-all">View All</a>
</section>

<footer class="footer">Copyright@2014 Brixton. All Right Reserved.<span>T10</span></footer>

</body>
</html>
```